Kelvard - Business Card Design

Design a modern masculine business card for our business

Target Market(s)

Private Market

Industry/Entity Type

Construction

Contact Information for Business Card

Company Name - Name of Person - Address - email address - contact number

Font styles to use
Serif
Sans Serif

Colors
0094D4
00A9DD
6FCCEA
C7EBF8
E9F6FB
00AB8E
00BBA5
67D7C9
C6EFE9
E9F9F6
F0912C
F2A743
F7CA91
FBE8D2
FDF5EE

Requirements
Must have
• Use company logo provided
Nice to have
• Company Logo

```html
<!DOCTYPE html>
<html lang="en">
<head>
<meta charset="utf-8">
<title>Kelvard – Business Card</title>
<link rel="stylesheet" href="https://fonts.googleapis.com/css2?family=Lato:wght@400;700;900&display=swap">
<style>
  :root {
    --backdrop: #3b3b3b;
    --ink: #111111;
    --paper: #ffffff;
    --accent: #f2732a;
  }
  * { margin: 0; padding: 0; box-sizing: border-box; }
  html, body { width: 1200px; height: 689px; overflow: hidden; }
  body {
    background: var(--backdrop);
    font-family: "Lato", sans-serif;
    position: relative;
  }
  .card {
    position: absolute;
    top: 196px;
    width: 520px;
    height: 298px;
    overflow: hidden;
  }
  .card--front {
    left: 45px;
    background: var(--paper);
    display: flex;
    align-items: center;
    justify-content: center;
  }
  .card--back { left: 635px; background: var(--ink); }
  .card__art { position: absolute; inset: 0; }
  .brand {
    font-weight: 900;
    text-transform: uppercase;
    line-height: 1;
  }
  .card--front .brand {
    color: var(--ink);
    font-size: 68px;
    letter-spacing: 2px;
    text-align: center;
  }
  .card--front .brand small {
    display: block;
    font-size: 20px;
    letter-spacing: 3px;
    margin-top: 8px;
  }
  .card--back .brand {
    position: absolute;
    left: 30px;
    bottom: 28px;
    color: var(--paper);
    font-size: 36px;
    letter-spacing: 1px;
  }
  .card--back .brand small {
    display: block;
    font-size: 11px;
    letter-spacing: 2px;
    margin-top: 5px;
  }
  .holder {
    position: absolute;
    right: 22px;
    top: 16px;
    text-align right;
    text-align: right;
    color: var(--paper);
  }
  .holder__name { font-weight: 900; font-size: 22px; letter-spacing: 0.5px; }
  .holder__role { font-size: 12px; margin-top: 2px; }
  .contact {
    position: absolute;
    left: 300px;
    top: 150px;
    list-style: none;
    color: var(--paper);
    font-size: 11.5px;
    line-height: 1.45;
  }
  .contact li { display: flex; align-items: flex-start; gap: 8px; }
  .contact svg { width: 10px; height: 10px; margin-top: 3px; flex: none; fill: var(--accent); }
</style>
</head>
<body>
  <section class="card card--front">
    <div class="brand">Kelvard<small>Construction, Inc</small></div>
  </section>

  <section class="card card--back">
    <svg class="card__art" viewBox="0 0 520 298" aria-hidden="true">
      <polygon points="0,0 520,0 520,76 178,128 0,210" fill="#f2732a"/>
      <polygon points="0,210 178,128 520,76 520,88 184,140 0,224" fill="#ffffff"/>
    </svg>

    <div class="holder">
      <div class="holder__name">ELRIC DANNER</div>
      <div class="holder__role">Founder &amp; CEO</div>
    </div>

    <ul class="contact">
      <li><svg viewBox="0 0 10 10"><path d="M5 0a3.5 3.5 0 0 0-3.5 3.5C1.5 6 5 10 5 10s3.5-4 3.5-6.5A3.5 3.5 0 0 0 5 0zm0 5a1.5 1.5 0 1 1 0-3 1.5 1.5 0 0 1 0 3z"/></svg><span>Your Address, City<br>State, Zip 1235</span></li>
      <li><svg viewBox="0 0 10 10"><path d="M2 0l2 2.5-1 1.2a6 6 0 0 0 3.3 3.3l1.2-1L10 8l-1.5 2C4 10 0 6 0 1.5z"/></svg><span>(123) 456-7890</span></li>
      <li><svg viewBox="0 0 10 10"><rect x="2.5" y="0" width="5" height="10" rx="1"/></svg><span>(231) 456-7890</span></li>
      <li><svg viewBox="0 0 10 10"><rect x="0" y="3" width="10" height="5"/><rect x="2" y="0" width="6" height="3"/><rect x="2" y="7" width="6" height="3"/></svg><span>(312) 456-7890</span></li>
      <li><svg viewBox="0 0 10 10"><path d="M0 2h10v6H0z"/><path d="M0 2l5 3.5L10 2" stroke="#111" stroke-width="0.8" fill="none"/></svg><span>info@yourwebsite.com</span></li>
      <li><svg viewBox="0 0 10 10"><circle cx="5" cy="5" r="5"/></svg><span>yourwebsite.com</span></li>
    </ul>

    <div class="brand">Kelvard<small>Construction, Inc</small></div>
  </section>
</body>
</html>
```